The Harlow Law Firm, PC

Dwight K. Harlow
Attorney at Law
physical address: 287 E. 9th Avenue
Greenville, NC 27019

mailing: P.O. Box 5843
Greenville, NC 27021

o. 555.416.2071
f. 555.416.8532

www.harlowlegal-ex.com

Industry/Entity Type

Attorney

Contact Information for Business Card

Attorney name
Office Phone number
Office Fax number
Mailing address and physical address
website address

Requirements
Must have
• Clean fresh design - I hate the website

```html
<!DOCTYPE html>
<html lang="en">
<head>
<meta charset="utf-8">
<title>The Harlow Law Firm, PC — Business Card</title>
<link href="https://fonts.googleapis.com/css2?family=PT+Sans&family=Tinos&display=swap" rel="stylesheet">
<style>
  :root {
    --backdrop: #d9d9d9;
    --paper: #f1f1f1;
    --paper-shade: #dcdcdc;
    --ink: #161616;
    --brand-blue: #1f5a9a;
    --tab-blue: #1d5c9e;
    --tab-rule: #8fb0d6;
    --icon-blue: #6f93c7;
    --light-text: #e9e9e9;
  }
  html, body {
    margin: 0;
    width: 1200px;
    height: 1000px;
    overflow: hidden;
    background: var(--backdrop);
  }
  .business-card {
    position: absolute;
    left: 100px;
    top: 210px;
    width: 1000px;
    height: 580px;
    border-radius: 50px;
    overflow: hidden;
    background: linear-gradient(180deg, var(--paper) 0%, var(--paper-shade) 100%);
    box-shadow: 0 12px 30px rgba(0,0,0,0.25);
    font-family: "PT Sans", sans-serif;
  }
  .firm-name {
    position: absolute;
    left: 55px;
    top: 95px;
    margin: 0;
    font-family: "Tinos", serif;
    font-weight: 400;
    font-size: 46px;
    line-height: 44px;
    color: var(--brand-blue);
    text-transform: uppercase;
    letter-spacing: 0.5px;
  }
  .firm-name .firm-small {
    font-size: 34px;
    color: var(--ink);
  }
  .firm-name .firm-line2 {
    display: block;
    padding-left: 48px;
  }
  .dark-band {
    position: absolute;
    left: 0;
    top: 255px;
    width: 100%;
    height: 240px;
    background: var(--ink);
  }
  .blue-stripe {
    position: absolute;
    left: 0;
    top: 495px;
    width: 100%;
    height: 12px;
    background: var(--brand-blue);
  }
  .attorney-tab {
    position: absolute;
    left: 460px;
    top: 70px;
    width: 510px;
    height: 205px;
    border-radius: 18px;
    background: var(--tab-blue);
    box-shadow: -4px 6px 10px rgba(0,0,0,0.25);
  }
  .tab-mark {
    position: absolute;
    left: 45px;
    top: 52px;
    width: 100px;
    height: 100px;
    border: 3px solid var(--tab-rule);
    box-sizing: border-box;
  }
  .attorney-name {
    position: absolute;
    left: 185px;
    top: 48px;
    margin: 0;
    font-family: "Tinos", serif;
    font-weight: 400;
    font-size: 38px;
    color: var(--tab-rule);
    white-space: nowrap;
  }
  .tab-rule {
    position: absolute;
    left: 185px;
    top: 104px;
    width: 285px;
    height: 3px;
    background: var(--tab-rule);
  }
  .attorney-title {
    position: absolute;
    left: 230px;
    top: 114px;
    margin: 0;
    font-size: 26px;
    color: var(--light-text);
  }
  .contact-item {
    position: absolute;
    color: var(--light-text);
  }
  .contact-item svg {
    position: absolute;
    left: 0;
    top: 12px;
  }
  .contact-label {
    position: absolute;
    left: 70px;
    top: 0;
    font-size: 26px;
    line-height: 30px;
    white-space: nowrap;
  }
  .contact-value {
    position: absolute;
    left: 70px;
    top: 30px;
    font-size: 24px;
    line-height: 30px;
    white-space: nowrap;
    letter-spacing: 0.5px;
  }
  .item-tel { left: 60px; top: 272px; }
  .item-fax { left: 60px; top: 340px; }
  .item-box { left: 60px; top: 408px; }
  .item-address { left: 520px; top: 318px; }
  .item-address .contact-value { font-size: 21px; }
  .website-box {
    position: absolute;
    left: 290px;
    top: 507px;
    width: 440px;
    height: 60px;
    background: var(--ink);
  }
  .website-box svg {
    position: absolute;
    left: 20px;
    top: 12px;
  }
  .website-url {
    position: absolute;
    left: 78px;
    top: 12px;
    font-family: "Tinos", serif;
    font-size: 28px;
    line-height: 36px;
    letter-spacing: 3px;
    color: var(--light-text);
    white-space: nowrap;
  }
</style>
</head>
<body>
<div class="business-card">
  <h1 class="firm-name"><span class="firm-small">The</span> Harlow<span class="firm-line2">Law Firm, <span class="firm-small">PC</span></span></h1>

  <div class="dark-band"></div>
  <div class="blue-stripe"></div>

  <div class="attorney-tab">
    <div class="tab-mark"></div>
    <p class="attorney-name">Dwight K. Harlow</p>
    <div class="tab-rule"></div>
    <p class="attorney-title">Attorney at Law</p>
  </div>

  <div class="contact-item item-tel">
    <svg width="40" height="38" viewBox="0 0 40 38" aria-hidden="true">
      <rect x="2" y="8" width="8" height="26" rx="3" fill="var(--icon-blue)"/>
      <rect x="12" y="4" width="26" height="30" rx="3" fill="var(--icon-blue)"/>
      <rect x="16" y="8" width="18" height="7" fill="var(--ink)"/>
      <g fill="var(--ink)">
        <rect x="16" y="19" width="4" height="3"/><rect x="23" y="19" width="4" height="3"/><rect x="30" y="19" width="4" height="3"/>
        <rect x="16" y="26" width="4" height="3"/><rect x="23" y="26" width="4" height="3"/><rect x="30" y="26" width="4" height="3"/>
      </g>
    </svg>
    <span class="contact-label">Tel:</span>
    <span class="contact-value">555-416-2071</span>
  </div>

  <div class="contact-item item-fax">
    <svg width="42" height="38" viewBox="0 0 42 38" aria-hidden="true">
      <rect x="10" y="2" width="22" height="12" fill="var(--icon-blue)"/>
      <rect x="2" y="12" width="38" height="18" rx="3" fill="var(--icon-blue)"/>
      <rect x="10" y="24" width="22" height="12" fill="var(--light-text)"/>
      <rect x="14" y="28" width="14" height="2" fill="var(--icon-blue)"/>
    </svg>
    <span class="contact-label">Fax:</span>
    <span class="contact-value">555-416-8532</span>
  </div>

  <div class="contact-item item-box">
    <svg width="42" height="38" viewBox="0 0 42 38" aria-hidden="true">
      <rect x="2" y="8" width="38" height="24" fill="var(--icon-blue)"/>
      <polyline points="2,8 21,22 40,8" fill="none" stroke="var(--ink)" stroke-width="2"/>
    </svg>
    <span class="contact-label">P.O. Box:</span>
    <span class="contact-value">5843 Greenville, NC 27021</span>
  </div>

  <div class="contact-item item-address">
    <svg width="38" height="40" viewBox="0 0 38 40" aria-hidden="true">
      <rect x="3" y="10" width="32" height="28" rx="4" fill="none" stroke="var(--icon-blue)" stroke-width="3"/>
      <circle cx="19" cy="10" r="6" fill="var(--icon-blue)"/>
      <line x1="19" y1="14" x2="19" y2="26" stroke="var(--icon-blue)" stroke-width="3"/>
      <circle cx="19" cy="27" r="4" fill="none" stroke="var(--icon-blue)" stroke-width="2"/>
    </svg>
    <span class="contact-label">address:</span>
    <span class="contact-value">287 E. 9th Avenue Greenville, NC 27019</span>
  </div>

  <div class="website-box">
    <svg width="36" height="36" viewBox="0 0 36 36" aria-hidden="true">
      <g fill="none" stroke="var(--icon-blue)" stroke-width="2.5">
        <circle cx="18" cy="18" r="15"/>
        <ellipse cx="18" cy="18" rx="7" ry="15"/>
        <line x1="3" y1="18" x2="33" y2="18"/>
        <line x1="18" y1="3" x2="18" y2="33"/>
      </g>
    </svg>
    <span class="website-url">www.harlowlegal-ex.com</span>
  </div>
</div>
</body>
</html>
```